Law Firm Needs a new Website Design

We need a new website design for our law firm located in Manhattan (Law Offices of Branford T. Quellsworth, PLLC).
We have an existing logo that we will to continue using, which can be found in www.QuellsworthLaw.example.
The Peak Counsel, Prime Advocates Logo should also be reflected near the bottom of the Home page.
The website will be 6 pages.

Deliverables:
I want a
1) home page,
2) About Us/Practice Areas page,
3) attorneys,
4) News and Articles page, and
5) Contact and Directions/Privacy Policy page.

The colors of my logo should be in the website.
I also like a touch of black and red.

The website should project "excellence."
We seek to provide the highest quality legal services.
We handle estate planning, wills, trusts, planning for people with disabilities, asset protection and preservation, Medicaid planning, hospital safe discharge, nursing home placement, powers of attorney, health care proxies, living wills, guardianships, probate, estate administration and related litigation.

I would like the colors of my Logo used (including shading where appropriate).
I also want some black on the borders and/or bottom and some red touches throughout the page.

My Logo should appear everywhere that "Law Offices Of Branford T. Quellsworth, PLLC" appears.
I want the badges for Peak counsel, Prime Advocates, Prime Legal Houses, and ZELK on the Home page.
I do not want too much text on the home page.

We would also like the website to have coding.
The final design should also communicate quality, expertise and stability.
Great start so far by the people who submitted designs.
Thank you.

Industry/Entity Type

Law Firm

Coding

Coded - Design and coding required

Number of Pages Required

5+ page

Colors
3276b5
ec1f27
474747

Requirements
Must have
• Please use my logo each time you mention Law Offices of Branford T. Quellsworth, PLLC. Please include the Peakcounsel, Prime Advocates, Prime Legal Houses and Zelk rating Badges on the web home page. I only wish to be contacted by phone. I am not including testimonials and am only using the New York City address.
Nice to have
• Prefer illustrations to photos regarding practice areas
Should not have
• Testimonials, contact me by email, free consultation.

```html
<!DOCTYPE html>
<html lang="en">
<head>
<meta charset="utf-8">
<title>Law Offices of Branford T. Quellsworth, PLLC</title>
<link href="https://fonts.googleapis.com/css2?family=Marcellus&family=Open+Sans:wght@400;600;700&display=swap" rel="stylesheet">
<style>
:root{
  --blue:#3276b5;
  --blue-dark:#245d93;
  --red:#ec1f27;
  --ink:#474747;
  --text:#6b6b6b;
  --light:#f5f5f5;
  --footer:#1e1e1e;
  --footer-base:#121212;
  --white:#ffffff;
}
*{box-sizing:border-box;margin:0;padding:0}
html,body{width:1200px;height:3930px;overflow:hidden}
body{font-family:"Open Sans",Arial,sans-serif;color:var(--ink);background:var(--white);position:relative}
.btn{display:inline-block;background:var(--red);color:var(--white);font-weight:700;font-size:14px;text-transform:uppercase;padding:0 26px;line-height:44px;border-radius:3px;letter-spacing:.3px}

/* header */
.site-header{height:138px;display:flex;align-items:center;justify-content:space-between;padding:0 62px 0 58px}
.brand{display:flex;align-items:center;gap:18px}
.brand-mark{width:62px;height:62px;background:var(--blue)}
.brand-name{font-family:"Marcellus",Georgia,serif;color:var(--ink);line-height:1.05;font-size:22px;text-align:center}
.brand-name .big{font-size:40px;display:block}
.header-phones{display:flex;gap:54px}
.phone{display:flex;align-items:center;gap:12px;font-size:19px;color:var(--ink)}
.phone-icon{width:34px;height:34px;border-radius:50%;border:2px solid var(--blue);display:flex;align-items:center;justify-content:center}

/* nav */
.main-nav{height:59px;background:var(--blue);display:flex;padding-left:32px}
.main-nav a{color:var(--white);font-size:13.5px;font-weight:700;text-transform:uppercase;line-height:59px;padding:0 24px;text-decoration:none}
.main-nav a.active{background:var(--blue-dark)}

/* hero */
.hero{height:550px;position:relative;background:linear-gradient(120deg,#2a1d10 0%,#6b5330 30%,#3b2c1a 55%,#15100b 100%)}
.hero-copy{position:absolute;right:60px;top:185px;text-align:right;color:var(--white)}
.hero-copy h1{font-family:"Marcellus",Georgia,serif;font-weight:400;font-size:42px;letter-spacing:1px}
.hero-copy p{font-family:"Marcellus",Georgia,serif;font-size:17px;margin:12px 0 22px}

/* welcome */
.welcome{height:689px;text-align:center;padding-top:82px}
.section-title{font-family:"Marcellus",Georgia,serif;font-weight:400;font-size:34px;color:#222;letter-spacing:.5px}
.welcome-intro{width:780px;margin:34px auto 0;font-size:14px;line-height:1.6;color:var(--text)}
.services{display:flex;justify-content:center;gap:60px;margin-top:80px}
.service{width:320px}
.service-icon{width:124px;height:124px;border-radius:50%;margin:0 auto;display:flex;align-items:center;justify-content:center;border:6px solid #dfe7f0;background:var(--blue)}
.service-icon.red{background:var(--red);border-color:#f6d4d5}
.service h3{font-size:17px;font-weight:400;color:#222;text-transform:uppercase;margin:44px auto 0;line-height:1.3;height:48px;width:270px}
.service p{font-size:13.5px;color:var(--text);line-height:1.65;margin-top:22px;padding:0 20px}

/* cta */
.cta{height:390px;position:relative;text-align:center;background:linear-gradient(180deg,#f3f3f3,#e4e4e4 60%,#ededed)}
.cta-inner{position:absolute;left:0;right:0;top:80px}
.cta h2{font-family:"Marcellus",Georgia,serif;font-weight:400;font-size:34px;color:var(--blue);letter-spacing:.5px}
.cta p{width:470px;margin:14px auto 28px;font-size:15px;line-height:1.45;color:#333}

/* practice areas */
.practice{height:930px;padding-top:75px;text-align:center}
.practice-grid{display:grid;grid-template-columns:repeat(3,327px);gap:70px 51px;justify-content:center;margin-top:86px}
.practice-card{background:var(--light);height:288px;border-bottom:4px solid var(--blue);position:relative}
.practice-photo{height:120px;background:linear-gradient(135deg,#c9d3df,#eef2f6 60%,#b9c6d6)}
.practice-photo.warm{background:linear-gradient(135deg,#d6c2ad,#f1e6da 55%,#c89a6e)}
.practice-photo.bright{background:linear-gradient(135deg,#e8784a,#cfd4da 55%,#7b8b9e)}
.practice-badge{width:44px;height:44px;border-radius:50%;background:var(--white);position:absolute;left:50%;top:98px;transform:translateX(-50%);display:flex;align-items:center;justify-content:center}
.practice-card h3{font-size:16px;font-weight:600;color:#222;margin-top:46px}
.practice-card p{font-size:12px;color:var(--text);line-height:1.75;margin-top:16px;white-space:nowrap}
.practice-card .more{background:var(--blue-dark);color:var(--white);font-size:12px;font-weight:600;text-transform:uppercase;line-height:36px;padding:0 20px;border-radius:2px;display:inline-block;margin-top:14px}
.practice-card.featured .practice-photo{height:80px}
.practice-card.featured .practice-badge{top:58px}
.practice-card.featured h3{margin-top:36px}
.practice-card.featured p{margin-top:12px}

/* attorneys */
.attorneys{height:587px;background:var(--blue);padding-top:68px;text-align:center}
.attorneys .section-title{color:var(--white)}
.attorney-row{display:flex;justify-content:center;gap:92px;margin-top:64px}
.attorney{width:495px;height:296px;background:var(--white);display:flex;text-align:left}
.attorney-photo{width:246px;height:296px;background:linear-gradient(160deg,#8a8f98,#4b4f58 60%,#2d3038)}
.attorney-photo.alt{background:linear-gradient(160deg,#8c6b4b,#b8977a 50%,#5a4232)}
.attorney-info{padding:14px 16px 0 16px;flex:1}
.attorney-info h3{font-family:"Marcellus",Georgia,serif;font-weight:400;font-size:19px;color:var(--blue);text-transform:uppercase;line-height:1.15}
.attorney-role{font-size:11.5px;color:#999;margin-top:6px}
.attorney-info p{font-size:13px;line-height:1.6;color:#444;margin:12px 0 16px}
.attorney-info .btn{font-size:13px;line-height:36px;padding:0 18px}

/* map */
.map{height:225px;background:linear-gradient(135deg,#e9e5dc,#f4f2ec 45%,#dfe6d8)}

/* footer */
.site-footer{height:328px;background:var(--footer);color:#bbb;position:relative;padding:40px 0 0 65px;display:flex}
.site-footer h4{color:var(--white);font-size:20px;font-weight:700}
.footer-contact{width:511px}
.footer-contact .lead{font-size:13px;line-height:1.55;color:#9a9a9a;margin-top:24px;width:360px}
.addresses{display:flex;gap:30px;margin-top:20px;align-items:flex-start}
.addr{display:flex;gap:8px;font-size:12.5px;line-height:1.45;color:#aaa;width:230px}
.rating-badges{display:flex;gap:10px}
.rating-badge{width:40px;height:40px;border-radius:50%;background:#3a3a3a;border:2px solid var(--blue)}
.rating-badge.square{border-radius:4px;border-color:var(--red)}
.contact-line{display:flex;align-items:center;gap:10px;font-size:13px;margin-top:12px;color:#bbb}
.footer-services{width:262px}
.service-lists{display:flex;gap:45px;margin-top:30px}
.service-lists ul{list-style:none}
.service-lists li{font-size:13px;color:#ddd;line-height:34px}
.footer-subscribe{width:300px}
.subscribe-form{display:flex;margin-top:32px}
.subscribe-form .field{width:242px;height:38px;background:var(--white)}
.subscribe-form .send{width:48px;height:38px;background:var(--red);display:flex;align-items:center;justify-content:center}
.subscribe-note{font-size:12.5px;color:#999;margin-top:16px;padding-bottom:18px;border-bottom:1px solid #3a3a3a}
.social{display:grid;grid-template-columns:130px 130px;margin-top:14px;font-size:13px;color:#ddd;line-height:30px}
.social span::before{content:"";display:inline-block;width:8px;height:8px;background:#ddd;margin-right:10px;vertical-align:middle}
.footer-base{height:34px;background:var(--footer-base);color:#888;font-size:11px;text-align:center;line-height:34px;letter-spacing:.3px}
</style>
</head>
<body>

<header class="site-header">
  <div class="brand">
    <div class="brand-mark"></div>
    <div class="brand-name">Law Offices of<span class="big">Branford T. Quellsworth</span>PLLC</div>
  </div>
  <div class="header-phones">
    <div class="phone"><span class="phone-icon"><svg width="16" height="16" viewBox="0 0 24 24"><path d="M6.6 10.8a15 15 0 0 0 6.6 6.6l2.2-2.2c.3-.3.7-.4 1-.2 1.1.4 2.3.6 3.6.6.6 0 1 .4 1 1V20c0 .6-.4 1-1 1A17 17 0 0 1 3 4c0-.6.4-1 1-1h3.5c.6 0 1 .4 1 1 0 1.3.2 2.5.6 3.6.1.3 0 .7-.2 1z" fill="#3276b5"/></svg></span>(212) 555-0148</div>
    <div class="phone"><span class="phone-icon"><svg width="16" height="16" viewBox="0 0 24 24"><rect x="4" y="8" width="16" height="12" rx="1" fill="none" stroke="#3276b5" stroke-width="2"/><rect x="7" y="3" width="10" height="6" fill="none" stroke="#3276b5" stroke-width="2"/><rect x="8" y="12" width="8" height="2" fill="#3276b5"/></svg></span>(212) 555-0172</div>
  </div>
</header>

<nav class="main-nav">
  <a class="active">Home</a><a>About Us</a><a>Practice Areas Page</a><a>Attorneys</a><a>News and Articles</a><a>Contact and Directions</a><a>Privacy Policy</a>
</nav>

<section class="hero">
  <div role="img" aria-label="Photo of brass scales of justice on a courtroom table" style="position:absolute;inset:0"></div>
  <div class="hero-copy">
    <h1>WE PROVIDE SOLUTIONS</h1>
    <p>We care about our clients and cultivating long-term relationships.</p>
    <span class="btn">Learn More</span>
  </div>
</section>

<section class="welcome">
  <h2 class="section-title">WELCOME BRANFORD T. QUELLSWORTH</h2>
  <p class="welcome-intro">Our firm was founded in 1993 by Branford T. Quellsworth, a member of the National Guild of Elder Counsel (NGEC) and an elder law practitioner for over 19 years. Our firm is uniquely positioned to provide quality legal advice and representation in regards to estate planning, wills, trusts, planning for people with disabilities, asset protection.</p>
  <div class="services">
    <div class="service">
      <div class="service-icon"><svg width="44" height="44" viewBox="0 0 24 24"><path d="M3 11 12 3l9 8" fill="none" stroke="#fff" stroke-width="2"/><path d="M6 10v10h12V10" fill="none" stroke="#fff" stroke-width="2"/><rect x="10" y="14" width="4" height="6" fill="#fff"/></svg></div>
      <h3>Real Estate and Planning Solutions</h3>
      <p>Estate planning is not just for the very wealthy or for senior citizens and often does not focus solely asset distribution after death.</p>
    </div>
    <div class="service">
      <div class="service-icon red"><svg width="44" height="44" viewBox="0 0 24 24"><rect x="5" y="3" width="14" height="18" rx="1" fill="none" stroke="#fff" stroke-width="2"/><path d="M8 8h8M8 12h8M8 16h5" stroke="#fff" stroke-width="2"/></svg></div>
      <h3>Medicaid Planning and Assistance</h3>
      <p>Estate planning is not just for the very wealthy or for senior citizens and often does not focus solely asset distribution after death.</p>
    </div>
    <div class="service">
      <div class="service-icon"><svg width="44" height="44" viewBox="0 0 24 24"><path d="M2 9 12 3l10 6z" fill="#fff"/><path d="M5 11v7M9.5 11v7M14.5 11v7M19 11v7" stroke="#fff" stroke-width="2"/><rect x="3" y="19" width="18" height="2" fill="#fff"/></svg></div>
      <h3>Powers of Attorney, Health Care Proxies</h3>
      <p>Estate planning is not just for the very wealthy or for senior citizens and often does not focus solely asset distribution after death.</p>
    </div>
  </div>
</section>

<section class="cta">
  <div role="img" aria-label="Faded photo of a courtroom interior" style="position:absolute;inset:0"></div>
  <div class="cta-inner">
    <h2>NEED AN ASSITANT FOR LEGAL HELP?</h2>
    <p>Etiam dignissim sit amet felis ac sagittis. Sed libero arcu, pharetra et ante euelementum scelerisque arcu. Curabitur sagittis non justo at ultri.</p>
    <span class="btn">Get and Appointment</span>
  </div>
</section>

<section class="practice">
  <h2 class="section-title">OUR PRACTICE AREAS</h2>
  <div class="practice-grid">
    <div class="practice-card featured">
      <div class="practice-photo" role="img" aria-label="Photo of a lawyer meeting clients"></div>
      <div class="practice-badge"><svg width="20" height="20" viewBox="0 0 24 24"><rect x="3" y="8" width="18" height="13" fill="none" stroke="#3276b5" stroke-width="2"/><path d="M3 13h18M12 8v13M8 8V5h8v3" fill="none" stroke="#3276b5" stroke-width="2"/></svg></div>
      <h3>Civil Litigation</h3>
      <p>Lorem ipsum dolor sit amet, consectetur adipiscing.<br>Odit qui minima praesentium illo obcaecat...</p>
      <span class="more">Read More</span>
    </div>
    <div class="practice-card">
      <div class="practice-photo" role="img" aria-label="Photo of business people shaking hands"></div>
      <div class="practice-badge"><svg width="22" height="22" viewBox="0 0 24 24"><path d="M2 12l5-4 5 3 5-3 5 4-5 4-5-2-5 2z" fill="#3276b5"/></svg></div>
      <h3>Business Taxation</h3>
      <p>Lorem ipsum dolor sit amet, consectetur adipiscing.<br>Odit qui minima praesentium illo obcaecat...</p>
    </div>
    <div class="practice-card">
      <div class="practice-photo" role="img" aria-label="Photo of hands reviewing financial documents"></div>
      <div class="practice-badge"><svg width="22" height="22" viewBox="0 0 24 24"><path d="M4 8h14l-3-3M20 16H6l3 3" fill="none" stroke="#3276b5" stroke-width="2"/></svg></div>
      <h3>Trade &amp; Finance law</h3>
      <p>Lorem ipsum dolor sit amet, consectetur adipiscing.<br>Odit qui minima praesentium illo obcaecat...</p>
    </div>
    <div class="practice-card">
      <div class="practice-photo bright" role="img" aria-label="Photo of a distressed driver after a car accident"></div>
      <div class="practice-badge"><svg width="22" height="22" viewBox="0 0 24 24"><path d="M3 15l2-6h14l2 6v3H3z" fill="#3276b5"/><circle cx="7" cy="18" r="2" fill="#fff" stroke="#3276b5" stroke-width="1.5"/><circle cx="17" cy="18" r="2" fill="#fff" stroke="#3276b5" stroke-width="1.5"/></svg></div>
      <h3>Accident Injuries</h3>
      <p>Lorem ipsum dolor sit amet, consectetur adipiscing.<br>Odit qui minima praesentium illo obcaecat...</p>
    </div>
    <div class="practice-card">
      <div class="practice-photo warm" role="img" aria-label="Photo of a family consulting a lawyer"></div>
      <div class="practice-badge"><svg width="22" height="22" viewBox="0 0 24 24"><circle cx="8" cy="7" r="3" fill="#3276b5"/><circle cx="16" cy="7" r="3" fill="#3276b5"/><path d="M3 20c0-5 10-5 10 0zM11 20c0-5 10-5 10 0z" fill="#3276b5"/></svg></div>
      <h3>Family law</h3>
      <p>Lorem ipsum dolor sit amet, consectetur adipiscing.<br>Odit qui minima praesentium illo obcaecat...</p>
    </div>
    <div class="practice-card">
      <div class="practice-photo warm" role="img" aria-label="Photo of a child studying with a parent"></div>
      <div class="practice-badge"><svg width="22" height="22" viewBox="0 0 24 24"><path d="M9 18h6M10 21h4M12 3a6 6 0 0 0-3 11v2h6v-2a6 6 0 0 0-3-11z" fill="none" stroke="#3276b5" stroke-width="2"/></svg></div>
      <h3>Education Law</h3>
      <p>Lorem ipsum dolor sit amet, consectetur adipiscing.<br>Odit qui minima praesentium illo obcaecat...</p>
    </div>
  </div>
</section>

<section class="attorneys">
  <h2 class="section-title">OUR EXPERT ATTORNEYS</h2>
  <div class="attorney-row">
    <div class="attorney">
      <div class="attorney-photo" role="img" aria-label="Portrait photo of attorney Branford T. Quellsworth"></div>
      <div class="attorney-info">
        <h3>Branford T. Quellsworth</h3>
        <p>Etiam dignissim sit amet felis ac sagittis. Sed libero arcu, pharetra et ante opos pil, elementum scel-erisque arcu. Curabitur sagittis non justo at ultricies odio ac.</p>
        <span class="btn">Read More</span>
      </div>
    </div>
    <div class="attorney">
      <div class="attorney-photo alt" role="img" aria-label="Portrait photo of attorney Delphine Marsh Quellsworth in a library"></div>
      <div class="attorney-info">
        <h3>Delphine Marsh Quellsworth</h3>
        <div class="attorney-role">Lawyer - Family Rights</div>
        <p>Etiam dignissim sit amet felis ac sagittis. Sed libero arcu, pharetra et ante opos pil, elementum scel-erisque arcu. Curabitur sagittis non justo at ultricies odio ac.</p>
        <span class="btn">Read More</span>
      </div>
    </div>
  </div>
</section>

<div class="map" role="img" aria-label="Street map of Midtown Manhattan marking the office location"></div>

<footer class="site-footer">
  <div class="footer-contact">
    <h4>Contact Us</h4>
    <p class="lead">We strive to maintain the dignity, independence and well-being of our clients and respond to them quickly.</p>
    <div class="addresses">
      <div class="addr"><svg width="12" height="16" viewBox="0 0 12 16"><path d="M6 0a6 6 0 0 0-6 6c0 4 6 10 6 10s6-6 6-10a6 6 0 0 0-6-6z" fill="#aaa"/><circle cx="6" cy="6" r="2" fill="#1e1e1e"/></svg><span>318 Larchmont Avenue, Suite 1204<br>New York, New York 10099</span></div>
      <div class="rating-badges" role="img" aria-label="Rating badges: Peak Counsel, Prime Advocates, Prime Legal Houses, Zelk">
        <span class="rating-badge"></span><span class="rating-badge square"></span><span class="rating-badge"></span><span class="rating-badge square"></span>
      </div>
    </div>
    <div class="contact-line"><svg width="14" height="14" viewBox="0 0 24 24"><path d="M6.6 10.8a15 15 0 0 0 6.6 6.6l2.2-2.2c.3-.3.7-.4 1-.2 1.1.4 2.3.6 3.6.6.6 0 1 .4 1 1V20c0 .6-.4 1-1 1A17 17 0 0 1 3 4c0-.6.4-1 1-1h3.5c.6 0 1 .4 1 1 0 1.3.2 2.5.6 3.6.1.3 0 .7-.2 1z" fill="#bbb"/></svg>(212) 555-0148</div>
    <div class="contact-line"><svg width="14" height="14" viewBox="0 0 24 24"><rect x="4" y="8" width="16" height="12" fill="#bbb"/><rect x="7" y="3" width="10" height="6" fill="none" stroke="#bbb" stroke-width="2"/></svg>(212) 555-0172</div>
    <div class="contact-line"><svg width="14" height="14" viewBox="0 0 24 24"><rect x="2" y="4" width="20" height="13" fill="none" stroke="#bbb" stroke-width="2"/><path d="M8 21h8" stroke="#bbb" stroke-width="2"/></svg>www.quellsworthlaw.example</div>
  </div>
  <div class="footer-services">
    <h4>Services</h4>
    <div class="service-lists">
      <ul><li>Home</li><li>Service</li><li>News</li><li>Bonds</li><li>Investments</li><li>Stocks</li></ul>
      <ul><li>About Us</li><li>Attorneys</li><li>Contact Us</li><li>Commodities</li><li>Retirement</li><li>Trends</li></ul>
    </div>
  </div>
  <div class="footer-subscribe">
    <h4>Subscribe</h4>
    <div class="subscribe-form"><div class="field"></div><div class="send"><svg width="18" height="14" viewBox="0 0 18 14"><rect x="1" y="1" width="16" height="12" fill="none" stroke="#fff" stroke-width="2"/><path d="M1 1l8 6 8-6" fill="none" stroke="#fff" stroke-width="2"/></svg></div></div>
    <p class="subscribe-note">Get Latest updates and offers.</p>
    <div class="social"><span>Fanbook</span><span>Circles Plus</span><span>Chirper</span><span>Linkwork</span></div>
  </div>
</footer>
<div class="footer-base">© 2016 WWW.QUELLSWORTHLAW.EXAMPLE ALL RIGHT RESERVED.</div>

</body>
</html>
```